Web Design for ROLV Air conditioning company

Hello,

I am calling on you for the modernization of the company's website
https://clarovent-services-techniques.fr/

The new one must include the new logo with the new graphic charter (color, style ...)

I'm looking for a simple design (less is more), a font written without Serif, the logo that brings a touch of color and modernity.

(maintenance and installation company for air conditioning and ventilation systems)
COLORS: in line with the logo

CHAPTER:

# PRESENTATION
# SERVICES
AIR CONDITIONING (ice cube icon)
HEATING (flame icon)
AIR TREATMENT (icon fan)
# ACHIEVEMENTS

# CONTACT
CONTACT FORM
GOOGLE MAPS

Target Market(s)

Showcase site for our customers

Coding

Coded - Design and coding required

Number of Pages Required

4 page

Font styles to use
Sans Serif

Colors
33b8a4
33a6d7
3176b5
ffffff

Requirements
Must have
• Clear and fluid navigation
a visual identity of the page with the logo
Should not have
• Overloaded.

```html
<!DOCTYPE html>
<html lang="en">
<head>
<meta charset="utf-8">
<title>ROLV – Clarovent Services Techniques</title>
<link href="https://fonts.googleapis.com/css2?family=Roboto:wght@400;500;700&family=Open+Sans:wght@400&display=swap" rel="stylesheet">
<style>
:root{
  --teal:#33b8a4;
  --teal-dark:#2e9e95;
  --blue:#33a6d7;
  --navy:#3176b5;
  --white:#ffffff;
  --ink:#2b2b2b;
  --text:#4a4a4a;
  --line:#c9c9c9;
  --footer:#35b59a;
  --grey-band:#8a8189;
  --panel:#575d5c;
}
*{box-sizing:border-box;margin:0;padding:0}
html,body{width:1200px;height:4130px;overflow:hidden}
body{position:relative;font-family:Roboto,Arial,sans-serif;color:var(--text);background:var(--white)}
.abs{position:absolute}
section,header,footer{position:absolute;left:0;width:1200px}

/* header */
.site-header{top:0;height:145px;background:var(--white)}
.topbar{left:545px;top:0;width:655px;height:55px;background:var(--teal);clip-path:polygon(26px 0,100% 0,100% 100%,0 100%);color:var(--white);font-size:15px}
.topbar .item{position:absolute;top:10px;display:flex;align-items:center;gap:12px}
.topbar .ico{width:36px;height:36px;border-radius:50%;background:var(--white);display:flex;align-items:center;justify-content:center}
.brand{left:112px;top:56px;display:flex;align-items:flex-end;gap:14px}
.brand-name{font-size:52px;font-weight:700;color:#2f3b44;letter-spacing:2px;line-height:1}
.brand-tag{font-size:11px;font-weight:500;color:var(--teal-dark);margin-bottom:6px}
.nav{left:510px;top:96px;display:flex;gap:30px;font-size:16px;color:var(--ink)}
.nav .active{color:var(--teal)}

/* hero */
.hero{top:145px;height:556px;background:linear-gradient(100deg,#7c8591 0%,#9aa3ad 35%,#b8bcc0 60%,#a9b25a 85%,#c9d84a 100%)}
.hero-shade{left:0;top:0;width:100%;height:100%;background:linear-gradient(90deg,rgba(30,40,60,.55),rgba(30,40,60,.1) 70%)}
.hero h1{left:113px;top:200px;font-size:31px;font-weight:700;color:var(--white);letter-spacing:.5px}
.hero p{left:113px;top:253px;width:560px;font-size:22px;line-height:40px;color:var(--white)}
.btn{position:absolute;display:flex;align-items:center;justify-content:center;border-radius:26px;font-weight:700;font-size:17px}
.hero .btn{left:108px;top:363px;width:162px;height:50px;background:var(--white);color:var(--teal-dark)}
.dots{left:570px;top:533px;display:flex;gap:16px}
.dots span{width:8px;height:8px;border-radius:50%;background:var(--white)}

/* about */
.about{top:701px;height:664px}
.about-bar{left:465px;top:334px;width:13px;height:204px;background:var(--teal-dark)}
.about-base{left:128px;top:537px;width:350px;height:25px;background:var(--teal)}
.about-img{left:100px;top:134px;width:367px;height:403px;border:5px solid #eee;background:linear-gradient(135deg,#e4e8ec,#b9c3cf 55%,#3d5f96);box-shadow:0 0 4px rgba(0,0,0,.2)}
.h2{font-size:40px;font-weight:700;color:var(--ink)}
.about h2{left:528px;top:84px}
.about .copy{left:528px;top:158px;width:562px;font-size:16px;line-height:34.3px;text-align:justify}
.btn-teal{background:linear-gradient(90deg,var(--teal-dark),var(--teal));color:var(--white)}
.about .btn{left:523px;top:530px;width:144px;height:50px}

/* services */
.services{top:1365px;height:615px;background:linear-gradient(180deg,#3596b7,#5bb98a);color:var(--white);text-align:center}
.services h2{left:0;width:100%;top:50px;font-size:40px;font-weight:700}
.services .lead{left:150px;width:900px;top:100px;font-size:16px;line-height:34px}
.card{position:absolute;top:223px;width:298px;text-align:center}
.card .photo{height:202px;border:1px solid #dfe6ea}
.card .badge{position:absolute;left:118px;top:167px;width:62px;height:62px;border-radius:50%;background:var(--white);display:flex;align-items:center;justify-content:center}
.card h3{margin-top:38px;font-size:21px;font-weight:700}
.card p{margin-top:8px;font-size:14px;line-height:25px}

/* achievements */
.achieve{top:1980px;height:591px}
.achieve h2{left:110px;top:108px}
.achieve .copy{left:110px;top:175px;width:470px;font-size:16px;line-height:34.3px;text-align:justify}
.achieve .btn{left:108px;top:480px;width:144px;height:50px}
.stats{left:618px;top:118px;width:474px;height:389px;background:radial-gradient(circle at 30% 55%,#6c7470,#4c5251 70%)}
.stat{position:absolute;width:167px;height:129px;border:1px solid rgba(255,255,255,.35);background:rgba(70,110,95,.35);color:var(--white);text-align:center}
.stat b{display:block;margin-top:18px;font-size:38px;font-weight:700}
.stat span{display:block;margin-top:6px;font-size:17px}

/* maintenance */
.maint{top:2571px;height:509px;background:var(--grey-band);color:var(--white)}
.maint-img{left:0;top:0;width:520px;height:509px;background:linear-gradient(90deg,#4c4d52,#b6aab3 50%,#d9ccd4 75%,var(--grey-band))}
.maint h2{left:530px;top:30px;font-size:40px;font-weight:700;line-height:64px}
.checks{left:530px;top:210px;list-style:none;font-size:19px}
.checks li{display:flex;align-items:center;gap:18px;height:44px}

/* contact */
.contact{top:3080px;height:605px;text-align:center}
.contact h2{left:0;width:100%;top:58px}
.contact .lead{left:0;width:100%;top:120px;font-size:17px;line-height:34px;color:var(--ink)}
.field{position:absolute;height:57px;border:1px solid var(--line);font-size:15px;color:var(--ink);text-align:left;padding:19px 20px}
.contact .btn{left:486px;top:472px;width:157px;height:52px;font-size:22px;font-weight:500}

/* footer */
.site-footer{top:3685px;height:445px;background:var(--footer);color:var(--white);font-size:16px}
.foot-brand{left:105px;top:58px;display:flex;align-items:flex-end;gap:10px}
.foot-brand .brand-name{font-size:36px;color:var(--white)}
.foot-brand .brand-tag{color:var(--white);font-size:10px;margin-bottom:3px}
.circle{position:absolute;width:44px;height:44px;border:2px solid var(--white);border-radius:50%;display:flex;align-items:center;justify-content:center}
.site-footer h4{font-size:21px;font-weight:700;letter-spacing:.5px}
.links{left:478px;top:115px;list-style:none;font-size:15px}
.links li{height:35px;display:flex;align-items:center;gap:10px}
.news-in{left:707px;top:113px;width:236px;height:50px;background:var(--white);color:#555;font-family:"Open Sans",sans-serif;font-size:12px;padding:17px 20px}
.news-btn{left:943px;top:113px;width:120px;height:50px;background:#000;color:var(--white);font-weight:500;display:flex;align-items:center;justify-content:center;font-size:17px}
.social{width:38px;height:38px;border:2px solid var(--white);border-radius:50%}
.copyright{left:0;width:1130px;top:384px;text-align:center;font-size:16px}
</style>
</head>
<body>

<header class="site-header">
  <div class="abs topbar">
    <div class="item" style="left:70px">
      <span class="ico"><svg width="18" height="14" viewBox="0 0 18 14"><rect x="1" y="1" width="16" height="12" rx="1" fill="none" stroke="#33b8a4" stroke-width="2"/><path d="M1 2l8 6 8-6" fill="none" stroke="#33b8a4" stroke-width="2"/></svg></span>
      contact@rolv-clim.fr
    </div>
    <div class="item" style="left:345px">
      <span class="ico"><svg width="18" height="18" viewBox="0 0 24 24"><path d="M6.6 10.8a15 15 0 006.6 6.6l2.2-2.2a1 1 0 011-.25 11.4 11.4 0 003.6.57 1 1 0 011 1V20a1 1 0 01-1 1A17 17 0 013 4a1 1 0 011-1h3.5a1 1 0 011 1 11.4 11.4 0 00.57 3.6 1 1 0 01-.25 1z" fill="#33b8a4"/></svg></span>
      Tel: 04 72 15 36 48
    </div>
  </div>
  <div class="abs brand"><span class="brand-name">ROLV</span><span class="brand-tag">CLAROVENT SERVICES TECHNIQUES</span></div>
  <nav class="abs nav"><span class="active">HOME</span><span>PRESENTATION</span><span>SERVICES</span><span>ACHIEVEMENTS</span><span>CONTACT</span></nav>
</header>

<section class="hero" role="img" aria-label="Technician in hard hat and mask cleaning a wall-mounted air conditioning unit">
  <div class="abs hero-shade"></div>
  <h1 class="abs">CLAROVENT-SERVICES-TECHNIQUES</h1>
  <p class="abs">Neque porro quisquam est qui dolorem ipsum quia dolor sit amet, consectetur, adipisci velit.</p>
  <span class="btn">GET STARTED</span>
  <div class="abs dots"><span></span><span></span><span></span></div>
</section>

<section class="about">
  <div class="abs about-bar"></div>
  <div class="abs about-base"></div>
  <div class="abs about-img" role="img" aria-label="Technician servicing an indoor air conditioning unit"></div>
  <h2 class="abs h2">ABOUT US</h2>
  <p class="abs copy">Sed ut perspiciatis unde omnis iste natus error sit voluptatem accusantium doloremque laudantium, totam rem aperiam, eaque ipsa quae ab illo inventore veritatis et quasi architecto beatae vitae dicta sunt explicabo. Nemo enim ipsam voluptatem quia voluptas sit aspernatur aut odit aut fugit, sed quia consequuntur magni dolores eos qui ratione voluptatem sequi nesciunt. Neque porro quisquam est, qui dolorem ipsum quia dolor sit amet, consectetur, adipisci velit, sed quia non numquam eius modi tempora incidunt ut labore et dolore magnam aliquam quaerat voluptatem. Ut enim ad minima veniam, quis nostrum exercitationem ullam corporis suscipit laboriosam, nisi ut aliquid ex ea commodi.</p>
  <span class="btn btn-teal">READ MORE</span>
</section>

<section class="services">
  <h2 class="abs">OUE SERVICES</h2>
  <p class="abs lead">At vero eos et accusamus et iusto odio dignissimos ducimus qui blanditiis praesentium voluptatum deleniti atque corrupti quos dolores et quas molestias excepturi sint occaecati cupiditate</p>
  <div class="card" style="left:112px">
    <div class="photo" role="img" aria-label="Outdoor air conditioning units" style="background:linear-gradient(90deg,#e8ecef,#cdd3d8 50%,#eef0f2)"></div>
    <span class="badge"><svg width="34" height="26" viewBox="0 0 34 26" fill="none" stroke="#333" stroke-width="1.6"><rect x="2" y="2" width="30" height="12" rx="2"/><path d="M6 10h22M9 18v5M14 18v5M19 18v5M24 18v5"/></svg></span>
    <h3>AIR CONDITIONING</h3>
    <p>Installation, Maintenance<br>Troubleshooting</p>
  </div>
  <div class="card" style="left:450px">
    <div class="photo" role="img" aria-label="Radiator thermostatic valve" style="background:linear-gradient(135deg,#8a8f93,#d6d9db 55%,#9a9ea2)"></div>
    <span class="badge"><svg width="30" height="32" viewBox="0 0 30 32" fill="none" stroke="#333" stroke-width="1.6"><path d="M4 8v20M10 6v22M16 6v22M22 6v22M26 8v20M2 28h26"/><path d="M15 2c3 3 3 6 0 8c-3-2-3-5 0-8z"/></svg></span>
    <h3>HEATING</h3>
    <p>Combustion control case<br>Keeping of the boiler room booklet</p>
  </div>
  <div class="card" style="left:788px">
    <div class="photo" role="img" aria-label="Industrial air treatment tanks" style="background:linear-gradient(90deg,#6f777c,#b5bcc0 50%,#7c8488)"></div>
    <span class="badge"><svg width="28" height="32" viewBox="0 0 28 32" fill="none" stroke="#333" stroke-width="1.6"><path d="M14 2c4 4 4 7 0 9c-4-2-4-5 0-9z"/><rect x="6" y="12" width="16" height="16" rx="3"/><path d="M3 30h22"/></svg></span>
    <h3>AIR TREATMENT</h3>
    <p>At vero eos et accusamus et iusto<br>odio dignissimos ducimus</p>
  </div>
</section>

<section class="achieve">
  <h2 class="abs h2">ACHIEVEMENTS</h2>
  <p class="abs copy">At vero eos et accusamus et iusto odio dignissimos ducimus qui blanditiis praesentium voluptatum deleniti atque corrupti quos dolores et quas molestias excepturi sint occaecati cupiditate Lorem Ipsum is simply dummy text of the printing and typesetting industry. Lorem Ipsum has been the industry's standard dummy text ever since the 1500s, when an unknown printer took a galley of type and scrambled it to make a type specimen book.</p>
  <span class="btn btn-teal">LEARN MORE</span>
  <div class="abs stats" role="img" aria-label="Pressure gauge background">
    <div class="stat" style="left:46px;top:50px"><b>280</b><span>Projects Finished</span></div>
    <div class="stat" style="left:260px;top:50px"><b>175</b><span>Happy Clients</span></div>
    <div class="stat" style="left:46px;top:209px"><b>140</b><span>Our Team</span></div>
    <div class="stat" style="left:260px;top:209px"><b>217</b><span>Hours of Work</span></div>
  </div>
</section>

<section class="maint">
  <div class="abs maint-img" role="img" aria-label="Outdoor air conditioning unit beside a house window"></div>
  <h2 class="abs">MAINTENANCE OF WATER<br>TREATMENT SYSTEM</h2>
  <ul class="abs checks">
    <li><svg width="26" height="24" viewBox="0 0 26 24" fill="none" stroke="#fff" stroke-width="2"><circle cx="11" cy="13" r="9"/><path d="M6 12l5 5L24 3"/></svg>Soft water</li>
    <li><svg width="26" height="24" viewBox="0 0 26 24" fill="none" stroke="#fff" stroke-width="2"><circle cx="11" cy="13" r="9"/><path d="M6 12l5 5L24 3"/></svg>Osmotic water</li>
    <li><svg width="26" height="24" viewBox="0 0 26 24" fill="none" stroke="#fff" stroke-width="2"><circle cx="11" cy="13" r="9"/><path d="M6 12l5 5L24 3"/></svg>maintenance of softeners</li>
    <li><svg width="26" height="24" viewBox="0 0 26 24" fill="none" stroke="#fff" stroke-width="2"><circle cx="11" cy="13" r="9"/><path d="M6 12l5 5L24 3"/></svg>treatment of liquid effluents</li>
    <li><svg width="26" height="24" viewBox="0 0 26 24" fill="none" stroke="#fff" stroke-width="2"><circle cx="11" cy="13" r="9"/><path d="M6 12l5 5L24 3"/></svg>Calibration of pH probes</li>
    <li><svg width="26" height="24" viewBox="0 0 26 24" fill="none" stroke="#fff" stroke-width="2"><circle cx="11" cy="13" r="9"/><path d="M6 12l5 5L24 3"/></svg>Conductivity probe calibration</li>
  </ul>
</section>

<section class="contact">
  <h2 class="abs h2">GET IN TOUCH</h2>
  <p class="abs lead">Lorem ipsum dolor sit amet, consectetur adipiscing elit. Sed vitae ante<br>Anibh ornare tristique laoreet ac odio.</p>
  <div class="field" style="left:245px;top:218px;width:303px">Your Name</div>
  <div class="field" style="left:580px;top:218px;width:302px">Your Last Name</div>
  <div class="field" style="left:245px;top:302px;width:303px">Phone</div>
  <div class="field" style="left:580px;top:302px;width:302px">Your Email</div>
  <div class="field" style="left:245px;top:381px;width:637px;height:62px">Message</div>
  <span class="btn btn-teal">SUBMIT</span>
</section>

<footer class="site-footer">
  <div class="abs foot-brand"><span class="brand-name">ROLV</span><span class="brand-tag">CLAROVENT SERVICES TECHNIQUES</span></div>
  <span class="circle" style="left:108px;top:108px"><svg width="16" height="22" viewBox="0 0 16 22"><path d="M8 1a7 7 0 017 7c0 5-7 13-7 13S1 13 1 8a7 7 0 017-7z" fill="#fff"/><circle cx="8" cy="8" r="2.5" fill="#35b59a"/></svg></span>
  <p class="abs" style="left:177px;top:138px;line-height:33px">14 Rue des Tilleuls<br>38100 GRENOBLE</p>
  <span class="circle" style="left:108px;top:221px"><svg width="18" height="18" viewBox="0 0 24 24"><path d="M6.6 10.8a15 15 0 006.6 6.6l2.2-2.2a1 1 0 011-.25 11.4 11.4 0 003.6.57 1 1 0 011 1V20a1 1 0 01-1 1A17 17 0 013 4a1 1 0 011-1h3.5a1 1 0 011 1 11.4 11.4 0 00.57 3.6 1 1 0 01-.25 1z" fill="#fff"/></svg></span>
  <p class="abs" style="left:170px;top:233px">Tel: 04 72 15 36 48</p>
  <span class="circle" style="left:108px;top:289px"><svg width="20" height="14" viewBox="0 0 20 14"><rect x="1" y="1" width="18" height="12" fill="none" stroke="#fff" stroke-width="1.6"/><path d="M1 1l9 7 9-7" fill="none" stroke="#fff" stroke-width="1.6"/></svg></span>
  <p class="abs" style="left:170px;top:300px">contact@rolv-clim.fr</p>

  <h4 class="abs" style="left:478px;top:60px">QUICKLINKS</h4>
  <ul class="abs links">
    <li><svg width="14" height="12" viewBox="0 0 14 12" fill="none" stroke="#fff" stroke-width="2"><path d="M1 1l5 5-5 5M7 1l5 5-5 5"/></svg>HOME</li>
    <li><svg width="14" height="12" viewBox="0 0 14 12" fill="none" stroke="#fff" stroke-width="2"><path d="M1 1l5 5-5 5M7 1l5 5-5 5"/></svg>PRESENTATION</li>
    <li><svg width="14" height="12" viewBox="0 0 14 12" fill="none" stroke="#fff" stroke-width="2"><path d="M1 1l5 5-5 5M7 1l5 5-5 5"/></svg>SERVICES</li>
    <li><svg width="14" height="12" viewBox="0 0 14 12" fill="none" stroke="#fff" stroke-width="2"><path d="M1 1l5 5-5 5M7 1l5 5-5 5"/></svg>ACHIEVEMENTS</li>
    <li><svg width="14" height="12" viewBox="0 0 14 12" fill="none" stroke="#fff" stroke-width="2"><path d="M1 1l5 5-5 5M7 1l5 5-5 5"/></svg>CONTACT</li>
  </ul>

  <h4 class="abs" style="left:698px;top:56px">NEWSLETTER SUBSCRIPTION</h4>
  <div class="abs news-in">Enter Your Newsletter</div>
  <div class="abs news-btn">SUBMIT</div>
  <span class="abs social" style="left:714px;top:184px"></span>
  <span class="abs social" style="left:763px;top:184px"></span>
  <span class="abs social" style="left:815px;top:184px"></span>
  <span class="abs social" style="left:869px;top:184px"></span>
  <span class="abs social" style="left:916px;top:184px"></span>

  <p class="abs copyright">Copyrights 2020. All rights reserved</p>
</footer>

</body>
</html>
```